Banner Ad for our online service

We would like a banner ad for our online service that provides video reviews for people seeking apartments--flatscout.org. We would like you to include our attached logo in the banner and would also like visuals representing our service. The banner should be 300x250 pixels and should include the following text:

-Moving to Boston?
-We review apartments so you don't have to.
-Order now and receive $40 gift card.

We're open to all ideas. Thanks.

```html
<!DOCTYPE html>
<html lang="en">
<head>
<meta charset="utf-8">
<title>FlatScout Banner – Moving to Boston?</title>
<link rel="stylesheet" href="https://fonts.googleapis.com/css2?family=Oswald:wght@400;500;600&display=swap">
<style>
  :root {
    --page-bg: #3a2418;
    --panel-dark: #262626;
    --panel-dark-top: #303030;
    --accent-orange: #f08a1c;
    --accent-orange-light: #ffb347;
    --text-white: #ffffff;
    --text-dark: #2a2a2a;
    --rule-grey: #4a4a4a;
    --logo-bg: #ffffff;
    --brand-grey: #3b3b3b;
  }
  * { margin: 0; padding: 0; box-sizing: border-box; }
  html, body {
    width: 1200px; height: 885px; overflow: hidden;
    background: var(--page-bg);
  }
  .stage {
    position: relative; width: 1200px; height: 885px;
  }
  .banner {
    position: absolute; left: 244px; top: 146px;
    width: 300px; height: 250px;
    transform: scale(2.372); transform-origin: 0 0;
    font-family: "Oswald", "Arial Narrow", sans-serif;
    overflow: hidden;
    box-shadow: 0 2px 6px rgba(0,0,0,.5);
  }
  .banner-shapes { position: absolute; inset: 0; }
  .headline {
    position: absolute; left: 0; top: 9px; width: 165px;
    text-align: center; text-transform: uppercase; line-height: 1;
  }
  .headline-kicker {
    color: var(--accent-orange); font-size: 21px; font-weight: 500;
  }
  .headline-city {
    color: var(--text-white); font-size: 31px; font-weight: 600; margin-top: 1px;
  }
  .pitch {
    position: absolute; left: 22px; top: 77px; width: 140px;
    text-transform: uppercase; color: var(--text-white);
    font-size: 17px; font-weight: 400; line-height: 17px;
  }
  .pitch .highlight { color: var(--accent-orange); }
  .offer {
    position: absolute; left: 18px; top: 172px; width: 140px;
    text-transform: uppercase; color: var(--text-white); line-height: 1;
  }
  .offer-lead { font-size: 9.5px; font-weight: 500; }
  .offer-value { font-size: 15px; font-weight: 400; margin-top: 3px; }
  .order-button {
    position: absolute; left: 18px; top: 210px; width: 117px; height: 24px;
    border-radius: 3px;
    background: linear-gradient(var(--accent-orange-light), var(--accent-orange));
    display: flex; align-items: center; justify-content: center; gap: 7px;
    color: var(--text-dark); font-size: 13px; font-weight: 500; text-transform: uppercase;
  }
  .order-button-icon {
    width: 13px; height: 13px; border-radius: 50%; background: var(--text-dark);
    display: flex; align-items: center; justify-content: center;
  }
  .brand {
    position: absolute; left: 178px; top: 213px;
    display: flex; align-items: center; gap: 5px;
  }
  .brand-dot { width: 16px; height: 16px; border-radius: 50%; background: var(--accent-orange); }
  .brand-name { color: var(--brand-grey); font-size: 17px; font-weight: 500; }
  .play-button {
    position: absolute; left: 213px; top: 94px; width: 40px; height: 40px;
    border-radius: 50%; background: rgba(20,20,20,.88);
    border: 2px solid var(--text-white);
    display: flex; align-items: center; justify-content: center;
  }
</style>
</head>
<body>
<div class="stage">
  <div class="banner">
    <svg class="banner-shapes" viewBox="0 0 300 250" width="300" height="250">
      <defs>
        <linearGradient id="panelShade" x1="0" y1="0" x2="0" y2="1">
          <stop offset="0" stop-color="var(--panel-dark-top)"/>
          <stop offset="1" stop-color="var(--panel-dark)"/>
        </linearGradient>
        <linearGradient id="streetTones" x1="0" y1="0" x2="0.4" y2="1">
          <stop offset="0" stop-color="#8fb6e0"/>
          <stop offset="0.25" stop-color="#9a4a3a"/>
          <stop offset="0.65" stop-color="#7a3428"/>
          <stop offset="0.85" stop-color="#5e6a3a"/>
          <stop offset="1" stop-color="#3a3a3a"/>
        </linearGradient>
      </defs>
      <rect width="300" height="250" fill="url(#panelShade)"/>
      <line x1="18" y1="160" x2="158" y2="160" stroke="var(--rule-grey)" stroke-width="1"/>
      <path d="M188 0 H300 V196 H168 Q170 90 188 0Z" fill="url(#streetTones)"
            role="img" aria-label="Photo of brick apartment buildings on a Boston street"/>
      <path d="M168 196 H300 V250 H162 Q164 222 168 196Z" fill="var(--logo-bg)"/>
      <path d="M188 0 Q170 90 168 196 Q164 222 162 250" fill="none"
            stroke="var(--accent-orange)" stroke-width="4"/>
    </svg>

    <div class="play-button">
      <svg width="14" height="16" viewBox="0 0 14 16"><path d="M2 1 L13 8 L2 15Z" fill="#fff"/></svg>
    </div>

    <div class="headline">
      <div class="headline-kicker">Moving to</div>
      <div class="headline-city">Boston?</div>
    </div>

    <p class="pitch">We review<br><span class="highlight">apartments</span><br>so you don’t<br>have to</p>

    <div class="offer">
      <div class="offer-lead">Order now and receive</div>
      <div class="offer-value">$40 gift card</div>
    </div>

    <div class="order-button">
      <span>Order now</span>
      <span class="order-button-icon">
        <svg width="6" height="7" viewBox="0 0 6 7"><path d="M1 0.5 L5.5 3.5 L1 6.5Z" fill="#ffb347"/></svg>
      </span>
    </div>

    <div class="brand">
      <span class="brand-dot"></span>
      <span class="brand-name">FlatScout</span>
    </div>
  </div>
</div>
</body>
</html>
```